TranquilPathbyHolt.com

I am looking to advertise our new business offering, tranquilpathbyholt.com, to our local hospice, nursing homes and hospitals. The idea was to have a nice, straightforward colorful postcard with a logo on the front and information on the back. Please peruse the site and utilize any information necessary to convey our concept. Here are the bullet points I'd like on the back of the card:

Tranquil Path by Holt is a cost-effective cremation offering that allows families to arrange for disposition of their loved one in the comfort of their own home.Our promise to you:

1) Your loved one will be transferred into the care of our funeral home with the utmost dignity and respect by the Holt staff. Upon arrival to our facility, they will never leave our care.

2) A trained director will contact the family, via phone, to assist with any questions or concerns.

3) By accessing www.tranquilpathbyholt.com, our intuitive site will take you step-by-step through the cremation arrangement process.

4) A positive identification will be made by the family prior to the cremation process. This will be done securely through our tranquilpathbyholt.com site.

Target Market(s)

Residents of Haywood County needing a low-cost disposition via cremation.

Industry/Entity Type

Business

Font styles to use
Serif

Colors

Designer to choose colors to be used in the design.

Requirements
Must have
• Tasteful design, somewhat of a serene front with a simple logo. The bullet points on the back.
Nice to have
• I have never designed a postcard so I'm relying on a professional to put the must haves.
Should not have
• I'm not looking to place our price on the brochure.

```html
<!DOCTYPE html>
<html lang="en">
<head>
<meta charset="utf-8">
<title>Tranquil Path by Holt — Postcard</title>
<link href="https://fonts.googleapis.com/css2?family=Crimson+Text:wght@400;600&family=Lato:wght@400;700&display=swap" rel="stylesheet">
<style>
  :root {
    --navy: #1d4a87;
    --navy-dark: #173d70;
    --slate: #5b5d62;
    --mist: #d4d5d8;
    --paper: #ffffff;
    --backdrop: #ecedef;
    --leaf-dark: #0f1a0f;
    --leaf-mid: #2c3b26;
  }
  * { box-sizing: border-box; margin: 0; padding: 0; }
  html, body { width: 1200px; height: 1200px; overflow: hidden; }
  body {
    background: var(--backdrop);
    position: relative;
    font-family: "Lato", sans-serif;
  }
  .postcard {
    position: absolute;
    left: 209px;
    width: 782px;
    height: 528px;
    overflow: hidden;
    box-shadow: 0 4px 18px rgba(0,0,0,.18);
    background: var(--paper);
  }
  /* ---------- Front ---------- */
  .postcard--front { top: 40px; }
  .front-photo {
    position: absolute; inset: 0;
    background:
      radial-gradient(ellipse at 55% 20%, rgba(90,110,80,.55), transparent 55%),
      radial-gradient(ellipse at 80% 80%, rgba(70,90,60,.45), transparent 50%),
      linear-gradient(160deg, var(--leaf-mid), var(--leaf-dark) 70%);
  }
  .front-frame {
    position: absolute; inset: 20px;
    border: 1px solid rgba(255,255,255,.75);
  }
  .front-band {
    position: absolute; left: 0; right: 0; top: 176px; height: 176px;
    background: rgba(255,255,255,.86);
    display: flex; align-items: center; justify-content: center; gap: 18px;
  }
  .brand-dot {
    width: 64px; height: 64px; border-radius: 50%;
    background: var(--navy);
    flex: none;
  }
  .brand-lockup {
    font-family: "Crimson Text", serif;
    color: var(--navy);
    text-align: center;
  }
  .brand-name { font-size: 56px; font-weight: 600; line-height: 1; }
  .brand-by { font-size: 22px; line-height: 1.3; margin-top: 6px; }
  .brand-tagline { font-size: 22px; line-height: 1.3; margin-top: 4px; }

  /* ---------- Back ---------- */
  .postcard--back { top: 632px; }
  .back-shapes { position: absolute; inset: 0; }
  .promise-panel {
    position: absolute; left: 70px; top: 36px; width: 300px;
    color: var(--paper);
    font-size: 12.5px; line-height: 1.35;
  }
  .promise-intro { text-align: justify; }
  .promise-heading { font-weight: 700; margin: 16px 0 10px; }
  .promise-list { list-style: none; }
  .promise-item {
    display: flex; gap: 8px; font-size: 11px; line-height: 1.32;
    margin-bottom: 12px; text-align: justify;
  }
  .promise-num {
    flex: none; width: 17px; height: 17px; border-radius: 50%;
    background: var(--paper); color: var(--navy);
    font-size: 10px; font-weight: 700;
    display: flex; align-items: center; justify-content: center;
  }
  .promise-url { text-align: center; font-size: 11px; font-weight: 700; margin-top: 18px; }
  .back-brand {
    position: absolute; left: 436px; top: 50px;
    display: flex; align-items: center; gap: 7px;
    font-family: "Crimson Text", serif; color: var(--navy);
  }
  .back-brand .brand-dot { width: 28px; height: 28px; }
  .back-brand .brand-name { font-size: 23px; font-weight: 400; }
  .back-brand .brand-by { font-size: 8px; margin-top: 1px; }
  .back-brand .brand-tagline { font-size: 8px; margin-top: 0; }
  .stamp-box {
    position: absolute; left: 678px; top: 30px; width: 76px; height: 84px;
    background: var(--mist);
  }
  .address-line {
    position: absolute; left: 462px; width: 296px; height: 1px;
    background: #b9bbc0;
  }
  .call-bar {
    position: absolute; left: 470px; top: 458px; width: 312px; height: 36px;
    background: var(--navy);
    border-radius: 18px 0 0 18px;
    color: var(--paper);
    display: flex; align-items: center; gap: 12px; padding-left: 18px;
    font-size: 16px; letter-spacing: .2px;
  }
  .call-phone { display: flex; align-items: center; gap: 6px; font-weight: 700; }
</style>
</head>
<body>

  <section class="postcard postcard--front">
    <div class="front-photo" role="img" aria-label="Photograph of white daisies against dark green foliage"></div>
    <div class="front-frame"></div>
    <div class="front-band">
      <span class="brand-dot"></span>
      <div class="brand-lockup">
        <div class="brand-name">Tranquil Path</div>
        <div class="brand-by">by HOLT</div>
        <div class="brand-tagline">The Best for Less</div>
      </div>
    </div>
  </section>

  <section class="postcard postcard--back">
    <svg class="back-shapes" width="782" height="528" viewBox="0 0 782 528">
      <path d="M0 340 H118 C150 400 152 460 138 502 H0 Z" fill="var(--slate)"/>
      <rect x="14" y="0" width="10" height="360" fill="var(--navy)"/>
      <path d="M36 0 H408 V300 C408 400 300 470 222 494 C144 470 36 400 36 300 Z" fill="var(--navy)"/>
      <path d="M44 0 V298 C44 392 148 458 222 482 C296 458 400 392 400 298 V0" fill="none" stroke="var(--paper)" stroke-width="3"/>
      <rect x="0" y="502" width="782" height="26" fill="var(--mist)"/>
    </svg>

    <div class="promise-panel">
      <p class="promise-intro"><strong>Tranquil Path</strong> by Holt is a cost-effective cremation offering that allows families to arrange for disposition of their loved one in the comfort of their own home.</p>
      <p class="promise-heading">Our promise to you:</p>
      <ol class="promise-list">
        <li class="promise-item"><span class="promise-num">1</span><span>Your loved one will be transferred into the care of our funeral home with the utmost dignity and respect by the Holt staff. Upon arrival to our facility, they will never leave our care.</span></li>
        <li class="promise-item"><span class="promise-num">2</span><span>A trained director will contact the family, via phone, to assist with any questions or concerns.</span></li>
        <li class="promise-item"><span class="promise-num">3</span><span>By accessing <strong>www.tranquilpathbyholt.com</strong>, our intuitive site will take you step-by-step through the cremation arrangement process.</span></li>
        <li class="promise-item"><span class="promise-num">4</span><span>A positive identification will be made by the family prior to the cremation process. This will be done securely through our tranquilpathbyholt.com site.</span></li>
      </ol>
      <p class="promise-url">www.tranquilpathbyholt.com</p>
    </div>

    <div class="back-brand">
      <span class="brand-dot"></span>
      <div class="brand-lockup">
        <div class="brand-name">Tranquil Path</div>
        <div class="brand-by">by HOLT</div>
        <div class="brand-tagline">The Best for Less</div>
      </div>
    </div>
    <div class="stamp-box"></div>
    <div class="address-line" style="top:246px"></div>
    <div class="address-line" style="top:293px"></div>
    <div class="address-line" style="top:334px"></div>

    <div class="call-bar">
      <span>CALL US NOW</span>
      <span class="call-phone">
        <svg width="16" height="16" viewBox="0 0 16 16" aria-hidden="true">
          <circle cx="8" cy="8" r="7.5" fill="var(--paper)"/>
          <path d="M5.2 4.2l1.4-.2.8 2-1 .8c.5 1.1 1.3 1.9 2.4 2.4l.8-1 2 .8-.2 1.4c-.1.4-.5.7-1 .6C7.4 10.6 5.4 8.6 4.6 5.2c-.1-.5.2-.9.6-1z" fill="var(--navy)"/>
        </svg>
        (828) 555-0142
      </span>
    </div>
  </section>

</body>
</html>
```